Brand New Solar Energy Business Needs a Flyer Design

We need an A5 double sided flyer for a new company in South Australia called Dorrit & Vale. We install home solar power systems and try to focus on quality of product and install.We also offer solar system servicing for existing systems which includes maintenance, cleaning and safety checks. Our web address is www.dorritandvale.com.au
We would like to see a design that's fresh and stands out in the mail box.
We feel the final design should communicate saving money on your electricity bills, local, quality and safety.
Target Market(s)
Home owners
Industry/Entity Type
Safety
Requirements
Must have
- A reference to our web site www.dorritandvale.com.au
A telephone number 0491638274

```html
<!DOCTYPE html>
<html lang="en">
<head>
<meta charset="utf-8">
<title>Dorrit &amp; Vale – Solar Flyer</title>
<link href="https://fonts.googleapis.com/css2?family=Arimo:wght@400;700&family=Oswald:wght@500;700&family=Roboto+Condensed:wght@700&display=swap" rel="stylesheet">
<style>
  :root {
    --brand-green: #1f8a3b;
    --leaf-green: #8cc63f;
    --lime-frame: #c8df3a;
    --sun-yellow: #fff200;
    --sky-blue: #1c9ad6;
    --white: #ffffff;
    --ink-shadow: rgba(0, 0, 0, 0.75);
  }
  * { box-sizing: border-box; margin: 0; padding: 0; }
  html, body { width: 845px; height: 1200px; overflow: hidden; background: #ffffff; }
  .flyer {
    position: relative;
    width: 845px;
    height: 1200px;
    overflow: hidden;
    background: var(--white);
    font-family: "Arimo", Arial, sans-serif;
  }

  /* Header */
  .call-box {
    position: absolute;
    left: 30px; top: 0;
    width: 315px; height: 151px;
    background: var(--brand-green);
    color: var(--white);
    font-weight: 700;
    font-size: 44px;
    line-height: 56px;
    padding: 18px 0 0 26px;
  }
  .brand {
    position: absolute;
    left: 362px; top: 22px;
    display: flex;
    align-items: center;
    gap: 16px;
  }
  .brand-dot {
    width: 100px; height: 100px;
    border-radius: 50%;
    background: var(--brand-green);
    flex: none;
  }
  .brand-name {
    font-weight: 700;
    font-size: 50px;
    color: var(--sky-blue);
    line-height: 1;
    white-space: nowrap;
  }
  .brand-tagline {
    font-size: 21px;
    color: var(--brand-green);
    margin-top: 10px;
    white-space: nowrap;
  }

  /* Hero */
  .hero-photo {
    position: absolute;
    left: 0; top: 151px;
    width: 845px; height: 479px;
    background: linear-gradient(160deg, #9fc3e6 0%, #c9dcef 30%, #4a6fa3 52%, #223e73 78%, #6b5448 100%);
  }
  .hero-headline {
    position: absolute;
    left: 0; top: 0;
    font-weight: 700;
    font-size: 74px;
    line-height: 1;
    color: var(--white);
    letter-spacing: -1px;
    text-shadow: 3px 3px 0 var(--ink-shadow), 0 0 8px var(--ink-shadow);
    white-space: nowrap;
  }
  .hero-headline .line-one { position: absolute; left: 196px; top: 295px; }
  .hero-headline .line-two { position: absolute; left: 362px; top: 378px; }

  /* Web band */
  .web-band {
    position: absolute;
    left: 0; top: 630px;
    width: 845px; height: 72px;
    display: flex; align-items: center; justify-content: center;
    font-weight: 700;
    font-size: 36px;
    color: var(--brand-green);
  }

  /* Lower section */
  .benefits-area {
    position: absolute;
    left: 0; top: 702px;
    width: 845px; height: 498px;
    background: var(--leaf-green);
  }
  .benefit-list {
    position: absolute;
    left: 24px; top: 32px;
    width: 420px;
    list-style: none;
  }
  .benefit {
    position: relative;
    padding-left: 57px;
    margin-bottom: 13px;
    font-family: "Roboto Condensed", "Arial Narrow", sans-serif;
    font-weight: 700;
    font-size: 27px;
    line-height: 34px;
    color: var(--white);
  }
  .benefit svg {
    position: absolute;
    left: 2px; top: 2px;
    width: 38px; height: 38px;
  }

  .offer-panel {
    position: absolute;
    left: 438px; top: 8px;
    width: 407px; height: 490px;
    background: var(--brand-green);
  }
  .offer-illustration {
    position: absolute;
    left: 56px; top: 36px;
    width: 315px; height: 238px;
    border: 8px solid var(--lime-frame);
    background: linear-gradient(135deg, #ffffff 0%, #f2e8e2 35%, #c96a4a 60%, #b9bcc2 100%);
  }
  .offer-free {
    position: absolute;
    left: 0; top: 290px;
    width: 407px;
    text-align: center;
    font-family: "Oswald", "Arial Narrow", sans-serif;
    font-weight: 700;
    font-size: 146px;
    line-height: 1;
    letter-spacing: 4px;
    color: var(--sun-yellow);
  }
  .offer-label {
    position: absolute;
    left: 0; top: 428px;
    width: 407px;
    text-align: center;
    font-family: "Roboto Condensed", "Arial Narrow", sans-serif;
    font-weight: 700;
    font-size: 34px;
    line-height: 40px;
    color: var(--white);
  }
</style>
</head>
<body>
<main class="flyer">

  <header>
    <div class="call-box">Call Us Now<br>0491638274</div>
    <div class="brand">
      <span class="brand-dot" aria-hidden="true"></span>
      <div>
        <div class="brand-name">Dorrit &amp; Vale</div>
        <div class="brand-tagline">Solar and Electrical Contractors</div>
      </div>
    </div>
  </header>

  <section class="hero-photo" role="img" aria-label="Photo of an installer fitting solar panels on a house roof under a blue sky"></section>
  <h1 class="hero-headline">
    <span class="line-one">$ave money with</span>
    <span class="line-two">Solar Power</span>
  </h1>

  <div class="web-band">Visit us : www.dorritandvale.com.au</div>

  <section class="benefits-area">
    <ul class="benefit-list">
      <li class="benefit">
        <svg viewBox="0 0 40 40" aria-hidden="true"><path d="M4 22 L15 33 L37 6" fill="none" stroke="#fff200" stroke-width="6" stroke-linecap="round" stroke-linejoin="round"/></svg>
        Save tonnes of greenhouse<br>gas emissions
      </li>
      <li class="benefit">
        <svg viewBox="0 0 40 40" aria-hidden="true"><path d="M4 22 L15 33 L37 6" fill="none" stroke="#fff200" stroke-width="6" stroke-linecap="round" stroke-linejoin="round"/></svg>
        South Australian Owned<br>solar energy business
      </li>
      <li class="benefit">
        <svg viewBox="0 0 40 40" aria-hidden="true"><path d="M4 22 L15 33 L37 6" fill="none" stroke="#fff200" stroke-width="6" stroke-linecap="round" stroke-linejoin="round"/></svg>
        Free electricity with<br>help from the Sun
      </li>
      <li class="benefit">
        <svg viewBox="0 0 40 40" aria-hidden="true"><path d="M4 22 L15 33 L37 6" fill="none" stroke="#fff200" stroke-width="6" stroke-linecap="round" stroke-linejoin="round"/></svg>
        Affordable Premium Solar<br>Sollutions, tailored for you
      </li>
      <li class="benefit">
        <svg viewBox="0 0 40 40" aria-hidden="true"><path d="M4 22 L15 33 L37 6" fill="none" stroke="#fff200" stroke-width="6" stroke-linecap="round" stroke-linejoin="round"/></svg>
        Wipe out your electricity<br>bills and protect against<br>future electricity price rises
      </li>
    </ul>

    <aside class="offer-panel">
      <div class="offer-illustration" role="img" aria-label="Illustration of a small house with solar panels beside a calculator and coloured bar charts"></div>
      <div class="offer-free">FREE</div>
      <div class="offer-label">SOLAR CONSULTATION</div>
    </aside>
  </section>

</main>
</body>
</html>
```